New Business Card Design For Re-Branded Company (New Logo)

We recently switched our DBA and had a new logo designed. We now need new business cards made around our new logo. We would like to stick with the color scheme in our logo: White, Orange, and Blue. We want to see original bold designs that reflect our position in the solar energy sector but we prefer simple over complicated.

We are curious about vertical designs so if you can translate your design onto a vertical layout we would be open to look at it. We especially like a few designs we have seen on here that are vertical with a black or very dark gray background. They have our logo on one side and then the normal vertical business card on the other side.

I have included a screenshot of one of the samples we like, labeled sample.jpg and a file we were given as an example of our logo on a dark background.

At the same time we are satisfied to stay with what we have always had in a horizontal format. If it's not a lot of extra work for you, designs that are submitted in both horizontal and vertical formats will be greatly appreciated.

Please submit your original, bold, clean designs for consideration. Contact us with any questions or comments that may arise.

Thank you and Good Luck,

RT

```html
<!DOCTYPE html>
<html lang="en">
<head>
<meta charset="utf-8">
<title>Solar Crest – Business Card</title>
<link href="https://fonts.googleapis.com/css2?family=Ubuntu:wght@400;500;700&display=swap" rel="stylesheet">
<style>
  :root {
    --blue: #1f6bb0;
    --blue-deep: #1a5f9f;
    --orange: #e8752a;
    --white: #ffffff;
    --paper: #eef0f2;
    --stage: #e4e2de;
  }
  * { box-sizing: border-box; margin: 0; padding: 0; }
  html, body { width: 1200px; height: 892px; overflow: hidden; }
  body {
    background: var(--stage);
    font-family: "Ubuntu", sans-serif;
    position: relative;
  }
  .card {
    position: absolute;
    top: 166px;
    width: 340px;
    height: 560px;
    box-shadow: 0 6px 18px rgba(0,0,0,0.18);
  }
  /* Front */
  .card-front {
    left: 235px;
    background: var(--blue);
    padding: 10px;
  }
  .front-inner {
    position: relative;
    width: 100%;
    height: 100%;
    background: var(--paper);
  }
  .front-brand {
    position: absolute;
    top: 92px;
    left: 0;
    right: 0;
    display: flex;
    align-items: center;
    justify-content: center;
    gap: 10px;
  }
  .brand-dot {
    width: 30px; height: 30px;
    border-radius: 50%;
    background: var(--orange);
  }
  .brand-name {
    font-weight: 700;
    font-size: 31px;
    letter-spacing: 0.5px;
    color: var(--blue);
    text-transform: uppercase;
  }
  .front-panel {
    position: absolute;
    left: 0; right: 0; bottom: 0;
    height: 330px;
    background: var(--blue);
    padding: 10px;
  }
  .panel-frame {
    width: 100%; height: 100%;
    border: 2px solid var(--white);
    position: relative;
    padding: 108px 0 0 34px;
  }
  .name-box {
    position: absolute;
    top: 12px; left: 0; right: 14px;
    height: 78px;
    background: var(--white);
    border: 2px solid var(--orange);
    padding: 10px 0 0 22px;
    color: var(--orange);
  }
  .name-box .person { font-size: 27px; font-weight: 700; line-height: 1; }
  .name-box .role { font-size: 14px; line-height: 1.2; }
  .contact-list { list-style: none; color: var(--white); font-size: 16px; }
  .contact-list li { display: flex; align-items: center; height: 26px; }
  .contact-list .icon {
    width: 14px; height: 14px;
    margin-right: 14px;
    flex: none;
  }
  .contact-list .indent { padding-left: 28px; }
  /* Back */
  .card-back {
    left: 625px;
    background: var(--blue-deep);
    overflow: hidden;
  }
  .back-brand {
    position: absolute;
    top: 50%; left: 50%;
    transform: translate(-50%, -50%) rotate(90deg);
    display: flex;
    align-items: center;
    gap: 14px;
    white-space: nowrap;
  }
  .back-brand .brand-dot {
    background: transparent;
    border: 4px solid var(--white);
    width: 40px; height: 40px;
  }
  .back-brand .brand-name { color: var(--white); font-size: 40px; }
  .back-web {
    position: absolute;
    left: 30px; top: 50%;
    transform: translate(-50%, -50%) rotate(90deg);
    transform-origin: center;
    color: rgba(255,255,255,0.85);
    font-size: 18px;
    margin-left: 20px;
  }
</style>
</head>
<body>
  <section class="card card-front" aria-label="Card front">
    <div class="front-inner">
      <div class="front-brand">
        <span class="brand-dot"></span>
        <span class="brand-name">Solar Crest</span>
      </div>
      <div class="front-panel">
        <div class="panel-frame">
          <div class="name-box">
            <div class="person">Dana Hollis</div>
            <div class="role">president</div>
          </div>
          <ul class="contact-list">
            <li><svg class="icon" viewBox="0 0 14 14"><rect width="14" height="14" rx="2" fill="#fff"/><path d="M4 3c-1 1-1 3 1 5s4 3 5 2l-1.5-1.5-1 .6L5.9 7.5l.6-1L5 5z" fill="#1f6bb0"/></svg>94 3181 2207</li>
            <li><svg class="icon" viewBox="0 0 14 14"><rect width="14" height="14" rx="2" fill="#fff"/><rect x="3" y="3" width="8" height="8" fill="none" stroke="#1f6bb0" stroke-width="1.3"/><path d="M5 6h4M5 8h4" stroke="#1f6bb0"/></svg>74 3902 6614</li>
            <li><svg class="icon" viewBox="0 0 14 14"><rect width="14" height="14" rx="2" fill="#fff"/><rect x="5" y="2.5" width="4" height="9" rx="1" fill="#1f6bb0"/></svg>94 7725 1049</li>
            <li><svg class="icon" viewBox="0 0 14 14"><rect width="14" height="14" rx="2" fill="#fff"/><path d="M7 12S3.5 8 3.5 6a3.5 3.5 0 0 1 7 0C10.5 8 7 12 7 12z" fill="#1f6bb0"/><circle cx="7" cy="6" r="1.2" fill="#fff"/></svg>PO Box 3172</li>
            <li class="indent">Marlow Heights NSW 2290</li>
            <li><svg class="icon" viewBox="0 0 14 14"><rect width="14" height="14" rx="2" fill="#fff"/><rect x="2.5" y="4" width="9" height="6" fill="none" stroke="#1f6bb0" stroke-width="1.2"/><path d="M2.5 4 7 7.5 11.5 4" fill="none" stroke="#1f6bb0" stroke-width="1.2"/></svg>solarcrest@email.com</li>
          </ul>
        </div>
      </div>
    </div>
  </section>

  <section class="card card-back" aria-label="Card back">
    <div class="back-brand">
      <span class="brand-dot"></span>
      <span class="brand-name">Solar Crest</span>
    </div>
    <div class="back-web">solarcrest.com</div>
  </section>
</body>
</html>
```